Finance Product Agency Business Card Design

We're an agency that provides products (service contracts, gap insurance, tire and wheel, etc) and support to dealership finance departments. We specialize in training finance producers to maximize their potential and also keep them up to date on the ever changing compliance and legal landscape. I'll attach an image of our logo, excited to see what you all come up with. Would also be interested in discussing our new website design with the winner.

Target Market(s)

auto dealerships

Industry/Entity Type

Business

Contact Information for Business Card

Mark Dolvery
Phone 317.624.5583
Fax 855.472.3308
email Mark.Dolvery@brightlanecoverage.example

Requirements
Must have
• basic contact information
Nice to have
• looking for something professional but modern

```html
<!DOCTYPE html>
<html lang="en">
<head>
<meta charset="utf-8">
<title>Brightlane Coverage — Business Card</title>
<link rel="stylesheet" href="https://fonts.googleapis.com/css2?family=Cinzel:wght@400&family=Oswald:wght@600&family=Roboto:wght@400;700&display=swap">
<style>
  :root {
    --page-bg: #d9d5d0;
    --card-bg: #eceeef;
    --card-edge: #f7f8f8;
    --ink: #1d2830;
    --ink-name: #2c3d4a;
    --ink-soft: #2a3238;
    --mark-dark: #1c2a33;
    --mark-light: #dfe3e5;
  }
  * { box-sizing: border-box; margin: 0; padding: 0; }
  html, body {
    width: 1200px;
    height: 969px;
    overflow: hidden;
    background: var(--page-bg);
  }
  .card {
    position: absolute;
    left: 100px;
    top: 200px;
    width: 1000px;
    height: 570px;
    background: linear-gradient(160deg, var(--card-edge) 0%, var(--card-bg) 60%, #e3e6e8 100%);
    box-shadow: 0 10px 30px rgba(0,0,0,0.18);
  }
  .brand {
    position: absolute;
    left: 60px;
    top: 76px;
    width: 390px;
    color: var(--ink);
    line-height: 1;
  }
  .brand-name {
    display: block;
    font-family: "Oswald", "Arial Narrow", sans-serif;
    font-weight: 600;
    font-size: 68px;
    letter-spacing: 0.5px;
  }
  .brand-sub {
    display: block;
    margin-top: 12px;
    font-family: "Cinzel", Georgia, serif;
    font-weight: 400;
    font-size: 25px;
    letter-spacing: 4px;
    color: var(--ink-soft);
  }
  .person {
    position: absolute;
    left: 52px;
    top: 294px;
    font-family: "Roboto", Arial, sans-serif;
    font-weight: 700;
    font-size: 42px;
    color: var(--ink-name);
  }
  .contact {
    position: absolute;
    left: 55px;
    top: 370px;
    list-style: none;
    font-family: "Roboto", Arial, sans-serif;
    font-weight: 400;
    color: var(--ink-soft);
  }
  .contact li {
    display: flex;
    align-items: center;
    height: 38px;
    font-size: 23px;
  }
  .contact .icon {
    width: 22px;
    height: 22px;
    margin: 0 20px 0 12px;
    fill: var(--ink-soft);
  }
  .contact .web-line { font-size: 21px; }
  .emblem-area {
    position: absolute;
    left: 478px;
    top: 34px;
    width: 500px;
    height: 508px;
    background: radial-gradient(circle at 50% 50%, var(--mark-dark) 0%, var(--mark-dark) 34%, #55636c 55%, var(--mark-light) 75%, rgba(236,238,239,0) 100%);
  }
</style>
</head>
<body>
  <div class="card">
    <div class="brand">
      <span class="brand-name">BRIGHTLANE</span>
      <span class="brand-sub">Coverage</span>
    </div>

    <div class="person">Mark Dolvery</div>

    <ul class="contact">
      <li>
        <svg class="icon" viewBox="0 0 24 24" aria-hidden="true">
          <path d="M6.6 10.8a15.1 15.1 0 0 0 6.6 6.6l2.2-2.2c.3-.3.7-.4 1-.2 1.1.4 2.3.6 3.6.6.6 0 1 .4 1 1V20c0 .6-.4 1-1 1A17 17 0 0 1 3 4c0-.6.4-1 1-1h3.5c.6 0 1 .4 1 1 0 1.3.2 2.5.6 3.6.1.3 0 .7-.2 1z"/>
        </svg>
        317.624.5583
      </li>
      <li>
        <svg class="icon" viewBox="0 0 24 24" aria-hidden="true">
          <path d="M6 2h10l2 2v4H6z M3 9h18c1 0 2 1 2 2v7h-4v4H5v-4H1v-7c0-1 1-2 2-2z M7 15v5h10v-5z"/>
        </svg>
        855.472.3308
      </li>
      <li class="web-line">www.brightlanecoverage.example</li>
      <li class="web-line">Mark.Dolvery@brightlanecoverage.example</li>
    </ul>

    <div class="emblem-area" role="img" aria-label="Large decorative brand emblem: dark circular mark with diamond checker pattern"></div>
  </div>
</body>
</html>
```